Bistro, bar, cafe, bottleshop and hotel

We are looking for a web design to best describe our hotel/pub and our new bistro, bar and cafe. The pub is called 'Hotel Brackenvale' and the bistro, bar, cafe is called 'Merrow's'. We would like our contact information clearly visable for any bookings etc.
Hotel Brackenvale
17 Quill Street
Brackenvale, Queensland 4380
hotelbrackenvale@quorimail.net
(07) 5290 1846
Hotel brackenvale is a old queensland colonial style hotel/pub, located on the corner of quill street and tarn street. It has old style pub accomodation thats has been newly rrefurbished and painted.
The bar has also has been refurbished. The spacious bar has a jukebox, dart board, pool table, gaming room and outdoor smoking area that overlooks the main street.
A new addition to the old style pub is 'Merrow's Bistro, Bar and Cafe' we are aiming for a family friendly atmosphere, a place to hold functions, place to have nice relaxing after work beverages with a few friends.
The newly extented drive thru bottleshop has a wide range of beer wine and spirits to meet just about every customers tastes.

```html
<!DOCTYPE html>
<html lang="en">
<head>
<meta charset="utf-8">
<title>Hotel Brackenvale</title>
<link href="https://fonts.googleapis.com/css2?family=Roboto+Condensed:wght@400;700&family=Libre+Baskerville:ital@0;1&family=Arimo&display=swap" rel="stylesheet">
<style>
:root{
  --plum:#4a2b2c;
  --cream:#f4e8c4;
  --frame:#e0d3a8;
  --tan:#e9c98a;
  --ink:#3b3434;
  --text:#1e1a1a;
  --tagline:#5a3a34;
  --red:#b3231f;
  --red-dark:#8f1714;
  --line:#d8c99c;
  --icon:#5b4a44;
}
*{margin:0;padding:0;box-sizing:border-box}
html,body{width:1182px;height:1200px;overflow:hidden;background:var(--cream)}
.page{position:relative;width:1182px;height:1200px;overflow:hidden;
  background:repeating-linear-gradient(90deg,rgba(255,255,255,.12) 0 2px,rgba(0,0,0,.02) 2px 4px),var(--cream);
  font-family:"Arimo",Arial,sans-serif;color:var(--text)}
.header{position:absolute;left:0;top:0;width:100%;height:61px;background:var(--plum);border-bottom:4px dotted var(--tan)}
.nav a{position:absolute;top:20px;font:400 19px "Roboto Condensed",sans-serif;color:var(--tan);text-decoration:none;white-space:nowrap}
.nav a.current{color:#f4dba6;text-decoration:underline}
.brand{position:absolute;left:492px;top:0;width:209px;height:98px;background:var(--plum);border-radius:0 0 105px 105px/0 0 45px 45px;
  display:flex;align-items:center;justify-content:center;padding-bottom:22px;
  font:700 36px "Roboto Condensed",sans-serif;color:#fff}
.call{position:absolute;right:103px;top:80px;text-align:right}
.call small{display:block;font:400 14px "Arimo",sans-serif;color:#a06a3c}
.call strong{display:block;font:400 26px "Arimo",sans-serif;color:#111;margin-top:1px}
.call svg{position:absolute;left:-78px;top:4px}
.slider{position:absolute;left:100px;top:136px;width:980px;height:467px;background:var(--frame);padding:12px}
.slider .photo{width:957px;height:389px;background:linear-gradient(180deg,#9fbde0 0%,#dfe6ee 28%,#a5623f 50%,#8a5a3a 70%,#4f4a45 85%,#5a6b3a 100%)}
.slider .arrow{position:absolute;top:173px;width:30px;height:65px;background:rgba(40,40,40,.75);display:flex;align-items:center;justify-content:center}
.slider .arrow.prev{left:12px}.slider .arrow.next{right:11px}
.booking{position:absolute;left:12px;top:401px;width:957px;height:54px;background:linear-gradient(#4d3435,#2e1f20)}
.booking > *{position:absolute}
.booking h2{left:36px;top:14px;font:400 21px "Libre Baskerville",serif;color:#fff;letter-spacing:-1px;white-space:nowrap}
.field{top:16px;height:22px;border:1px solid #7a6a64;background:rgba(0,0,0,.15);font:400 11px "Arimo",sans-serif;color:#fff;display:flex;align-items:center;justify-content:space-between;padding:0 4px 0 6px}
.field .caret{width:16px;height:16px;background:#fff;display:flex;align-items:center;justify-content:center}
.submit{left:826px;top:13px;background:var(--red);color:#fff;font:400 14px "Libre Baskerville",serif;padding:5px 7px;border:1px solid var(--red-dark)}
.tagline{position:absolute;left:100px;top:625px;width:983px;height:77px;border-top:1px solid var(--line);border-bottom:1px solid var(--line);
  font:italic 400 19px/26px "Libre Baskerville",serif;color:var(--tagline);text-align:center;padding-top:10px}
.col{position:absolute;top:740px}
.col h2{font:400 37px "Roboto Condensed",sans-serif;color:var(--ink);letter-spacing:.3px}
.frame{width:310px;height:137px;background:var(--frame);padding:9px;margin:12px 0 0 -2px}
.frame .pic{width:100%;height:100%}
.col p{font:400 13px/18px "Arimo",sans-serif;margin-top:18px;width:310px}
.more{position:absolute;width:108px;height:28px;background:var(--red);color:#fff;font:400 11px "Libre Baskerville",serif;display:flex;align-items:center;justify-content:center;text-decoration:none;
  clip-path:polygon(0 0,100% 0,96% 50%,100% 100%,0 100%,4% 50%)}
.contact address{font:normal 400 14px/22px "Arimo",sans-serif;margin:10px 0 0 3px}
.divider{position:absolute;left:845px;top:922px;width:207px;border-top:1px solid var(--line)}
.follow{position:absolute;left:850px;top:940px;font:400 27px "Roboto Condensed",sans-serif;color:var(--ink)}
.social{position:absolute;top:983px;width:38px;height:38px;background:var(--icon);border-radius:4px}
.footer{position:absolute;left:0;top:1133px;width:100%;height:67px;background:var(--plum)}
.footer nav{position:absolute;left:114px;top:24px;font:400 15px "Roboto Condensed",sans-serif;color:var(--tan)}
.footer nav a{color:var(--tan);text-decoration:none}
.footer nav span{margin:0 10px}
.footer .copy{position:absolute;right:103px;top:24px;font:400 15px "Roboto Condensed",sans-serif;color:var(--tan)}
</style>
</head>
<body>
<div class="page">
  <header class="header">
    <nav class="nav">
      <a class="current" href="#" style="left:136px">Home</a>
      <a href="#" style="left:234px">Front Bar</a>
      <a href="#" style="left:364px">Merrow's Bistro</a>
      <a href="#" style="left:725px">Bar &amp; Cafe</a>
      <a href="#" style="left:851px">Accomodation</a>
      <a href="#" style="left:998px">Contact Us</a>
    </nav>
  </header>
  <div class="brand">Brackenvale</div>

  <div class="call">
    <svg width="54" height="44" viewBox="0 0 54 44" aria-hidden="true">
      <path d="M6 16c4-10 38-10 42 0l-7 5-6-5H19l-6 5z" fill="#1f2a5a"/>
      <path d="M12 22h30l6 20H6z" fill="#e8a21f"/>
      <circle cx="27" cy="31" r="7" fill="#f6d27a" stroke="#a36b10" stroke-width="2"/>
    </svg>
    <small>Your first visit? Call for info</small>
    <strong>(07) 5290 1846</strong>
  </div>

  <section class="slider">
    <div class="photo" role="img" aria-label="Street view of the two-storey colonial hotel with balconies on a sunny day"></div>
    <div class="arrow prev"><svg width="14" height="28" viewBox="0 0 14 28"><path d="M12 2 3 14l9 12" stroke="#fff" stroke-width="3" fill="none"/></svg></div>
    <div class="arrow next"><svg width="14" height="28" viewBox="0 0 14 28"><path d="M2 2l9 12-9 12" stroke="#fff" stroke-width="3" fill="none"/></svg></div>
    <form class="booking">
      <h2>BOOK A ROOM:</h2>
      <div class="field" style="left:223px;width:114px">Check in
        <svg width="16" height="14" viewBox="0 0 16 14"><rect x=".5" y="1.5" width="15" height="12" fill="none" stroke="#aaa"/><path d="M1 5h14M4 8h8M4 11h8" stroke="#aaa"/></svg></div>
      <div class="field" style="left:342px;width:114px">Check out
        <svg width="16" height="14" viewBox="0 0 16 14"><rect x=".5" y="1.5" width="15" height="12" fill="none" stroke="#aaa"/><path d="M1 5h14M4 8h8M4 11h8" stroke="#aaa"/></svg></div>
      <div class="field" style="left:485px;width:201px">Select room type<span class="caret"><svg width="8" height="5"><path d="M0 0h8L4 5z" fill="#333"/></svg></span></div>
      <div class="field" style="left:700px;width:109px">No. of rooms<span class="caret"><svg width="8" height="5"><path d="M0 0h8L4 5z" fill="#333"/></svg></span></div>
      <span class="submit">SUBMIT</span>
    </form>
  </section>

  <p class="tagline">Lorem ipsum dolor sit amet, consectetur adipiscing elit. Pellentesque vel mauris a diam convallis dapibus<br>vel eget tortor. Vestibulum ante ipsum primis in faucibus orci luctus.</p>

  <section class="col" style="left:103px">
    <h2>WELCOME!</h2>
    <div class="frame"><div class="pic" role="img" aria-label="Hotel building seen across the roundabout" style="background:linear-gradient(180deg,#b8cce4 0%,#e5e9ee 35%,#9a5d3e 55%,#6b5a4a 75%,#55575a 100%)"></div></div>
    <p>Lorem ipsum dolor sit amet, consectetur adipiscing elit, sed do eiusmod tempor incididunt ut labore et dolore magna aliqua. Ut enim ad quis nostrud exercitation ullamco laboris nisi ut aliquip ex ea commodo consequat. Duis aute....</p>
  </section>
  <a class="more" href="#" style="left:101px;top:1051px">READ MORE</a>

  <section class="col" style="left:476px">
    <h2>BAR AND CAFE</h2>
    <div class="frame"><div class="pic" role="img" aria-label="Refurbished bar with white stools and a long counter" style="background:linear-gradient(90deg,#6f7c86 0%,#c9ccd0 35%,#e8e6e2 55%,#9aa0a4 75%,#c7c7b6 100%)"></div></div>
    <p>Lorem ipsum dolor sit amet, consectetur adipiscing elit, sed do eiusmod tempor incididunt ut labore et dolore magna aliqua. Ut enim ad quis nostrud exercitation ullamco laboris nisi ut aliquip ex ea commodo consequat. Duis aute....</p>
  </section>
  <a class="more" href="#" style="left:474px;top:1052px">READ MORE</a>

  <section class="col contact" style="left:845px">
    <h2>CONTACT US</h2>
    <address>Hotel Brackenvale<br>17 Quill Street<br>Brackenvale, Queensland 4380<br>hotelbrackenvale@quorimail.net<br>(07) 5290 1846</address>
  </section>
  <div class="divider"></div>
  <h3 class="follow">FOLLOW US</h3>
  <a class="social" href="#" aria-label="Social page one" style="left:850px"></a>
  <a class="social" href="#" aria-label="Social page two" style="left:901px"></a>
  <a class="social" href="#" aria-label="Social page three" style="left:951px"></a>
  <a class="social" href="#" aria-label="News feed" style="left:1001px"></a>
  <a class="more" href="#" style="left:849px;top:1052px">READ MORE</a>

  <footer class="footer">
    <nav><a href="#">Home</a><span>|</span><a href="#">Front Bar</a><span>|</span><a href="#">Merrow's Bistro</a><span>|</span><a href="#">Bar &amp; Cafe</a><span>|</span><a href="#">Accomodation</a><span>|</span><a href="#">Contact Us</a></nav>
    <div class="copy">Copyright © 2013 Hotel Brackenvale.</div>
  </footer>
</div>
</body>
</html>
```